Closing our Brindel Office

I currently have a three location eye care practice located in Spokane Valley, Airway Heights and Brindel Marketways. We are closing our Brindel location and hope to see these patients at our other practices.
Updates

I would like something that comes across as more friendly and appreciative... "Thank you for seeing us at our Brindel Marketway clinic. This location has now closed. We hope to continue to provide care for you at our Airway Heights or Spokane Valley locations. -Dr Tavo Rennick, Mila and Odette This will be on a postcard, so it needs to have space for address and stamp. Must have picture of the three of us on the front, and picture of both locations (wide view showing mural) on the back. (okay to include or leave out picture of me on back) Please include address with pictures: Spokane Valley Clinic- 48316 E Carrow Ln. Airway Heights Clinic - 3094 S Pimbury Rd. Also need to include Phone number : 509-418-2639, www.brightlenscare.com, and hello@brightlenscare.com.

Target Market(s)

Current Brindel patients

Font styles to use
Serif
Sans Serif

Requirements
Must have
• Photo of myself and two staff.
• Photo of Airway Heights and Valley office
• Photo with mural to left is my Airway office. Photo with mural to the right is Spokane Valley (Marlowe Exit)
• Phone # 509-418-2639. www.brightlenscare.com
Nice to have
• Front of card with photo of myself, Mila (darker hair on left) and Odete (longer hair on right)
• Back of card with images of both other clinics and small photo of myself

```html
<!DOCTYPE html>
<html lang="en">
<head>
<meta charset="utf-8">
<title>Brindel Closing Postcard</title>
<link rel="stylesheet" href="https://fonts.googleapis.com/css2?family=Dosis:wght@300;400&family=Roboto+Condensed:wght@400;700&family=Mrs+Saint+Delafield&display=swap">
<style>
  :root {
    --stage: #bdb8b8;
    --blue: #0a84cc;
    --blue-deep: #1565b8;
    --blue-dark: #1d3f8a;
    --navy: #1e2a5a;
    --red: #e0212a;
    --ink: #2a2d33;
    --white: #ffffff;
    --line: #c9c9c9;
    --stamp: #cfd0d2;
  }
  * { margin: 0; padding: 0; box-sizing: border-box; }
  html, body { width: 1200px; height: 1200px; overflow: hidden; background: var(--stage); }
  .canvas { position: relative; width: 1200px; height: 1200px; }

  .card { position: absolute; background: var(--white); overflow: hidden; }
  .card--front { left: 197px; top: 29px; width: 779px; height: 550px; }
  .card--back { left: 192px; top: 612px; width: 790px; height: 558px; }

  .card-art { position: absolute; inset: 0; }

  .brand { position: absolute; display: flex; align-items: center; gap: 8px;
    font-family: "Roboto Condensed", sans-serif; font-weight: 700; color: var(--navy);
    letter-spacing: 0.5px; white-space: nowrap; }
  .brand__dot { width: 18px; height: 18px; border-radius: 50%; background: var(--blue-deep); }

  /* front */
  .front-kicker { position: absolute; left: 139px; top: 127px; font-family: "Dosis", sans-serif;
    font-weight: 300; font-size: 32px; line-height: 40px; color: var(--ink); letter-spacing: 0.5px; white-space: nowrap; }
  .script { position: absolute; font-family: "Mrs Saint Delafield", cursive; color: var(--red); white-space: nowrap; }
  .front-thanks { left: 136px; top: 184px; font-size: 106px; line-height: 1; }
  .front-message { position: absolute; left: 139px; top: 284px; font-family: "Dosis", sans-serif;
    font-weight: 300; font-size: 24px; line-height: 38px; color: var(--ink); white-space: nowrap; }
  .front-signature { left: 139px; top: 488px; font-size: 40px; line-height: 1; }

  .front-brand { right: 34px; top: 92px; font-size: 22px; }
  .contact { position: absolute; right: 16px; display: flex; align-items: center; gap: 6px;
    font-family: "Roboto Condensed", sans-serif; font-weight: 700; color: var(--blue); white-space: nowrap; }
  .contact--phone { top: 145px; font-size: 34px; line-height: 40px; }
  .contact--email { top: 192px; font-size: 21px; line-height: 26px; }
  .contact--web { top: 224px; font-size: 21px; line-height: 26px; }
  .contact svg { flex: none; }

  /* back */
  .back-brand { left: 28px; top: 86px; font-size: 22px; }
  .back-find { left: 50px; top: 128px; font-size: 80px; line-height: 1; }
  .clinic-photo { position: absolute; }
  .clinic-photo--airway { left: 61px; top: 202px; width: 257px; height: 144px;
    background: linear-gradient(90deg, #2e3b47 0%, #3e4c58 55%, #b9b4ae 62%, #8a8580 100%); }
  .clinic-photo--valley { left: 64px; top: 394px; width: 251px; height: 164px;
    background: linear-gradient(90deg, #a9a4a0 0%, #7d7872 35%, #3a4652 45%, #2f3a44 70%, #7a4f2c 100%); }
  .address-strip { position: absolute; left: 0; top: 346px; width: 380px; height: 46px; background: var(--white);
    display: flex; align-items: center; font-family: "Roboto Condensed", sans-serif; }
  .address { padding-left: 15px; width: 186px; }
  .address + .address { border-left: 3px solid var(--red); padding-left: 16px; width: 194px; }
  .address__name { font-weight: 700; font-size: 17px; color: var(--blue); line-height: 20px; }
  .address__street { font-weight: 400; font-size: 16px; color: var(--blue-deep); line-height: 19px; }

  .stamp-box { position: absolute; left: 694px; top: 16px; width: 114px; height: 130px; background: var(--stamp); }
  .mail-line { position: absolute; left: 398px; width: 322px; height: 2px; background: var(--line); }
</style>
</head>
<body>
<div class="canvas">

  <section class="card card--front" aria-label="Postcard front">
    <svg class="card-art" width="779" height="550" viewBox="0 0 779 550">
      <defs>
        <linearGradient id="frontWash" x1="0" y1="0" x2="1" y2="0">
          <stop offset="0" stop-color="#0d86cf"/>
          <stop offset="0.3" stop-color="#2a93d6"/>
          <stop offset="0.62" stop-color="#d6e8f6"/>
          <stop offset="0.74" stop-color="#ffffff"/>
        </linearGradient>
        <linearGradient id="teamTone" x1="0" y1="0" x2="1" y2="1">
          <stop offset="0" stop-color="#cfc9c4"/>
          <stop offset="0.5" stop-color="#8a6a52"/>
          <stop offset="1" stop-color="#1c1c22"/>
        </linearGradient>
      </defs>
      <rect width="779" height="550" fill="url(#frontWash)"/>
      <path d="M0 0 H779 V60 Q650 -10 470 70 Q300 130 0 42 Z" fill="#0a7fc9"/>
      <path d="M0 42 Q300 130 470 70 Q650 -10 779 60" fill="none" stroke="#ffffff" stroke-width="3"/>
      <path d="M0 56 Q300 142 470 84 Q640 14 779 72" fill="none" stroke="#ffffff" stroke-width="1.5" opacity="0.8"/>
      <path d="M250 40 Q300 200 150 330 Q60 420 40 550" fill="none" stroke="#1d3f8a" stroke-width="3" opacity="0.6"/>
      <circle cx="666" cy="430" r="166" fill="#0a84cc"/>
      <circle cx="666" cy="430" r="156" fill="url(#teamTone)" role="img" aria-label="Photo of Dr Rennick with Mila and Odete"/>
    </svg>

    <p class="front-kicker">A LITTLE NOTE TO SAY A BIG</p>
    <p class="script front-thanks">Thank You</p>
    <p class="front-message">for seeing us at our Brindel Marketway<br>clinic. This location has now closed.<br>We hope to continue to provide care<br>for you at our Airway Heights or<br>Spokane Valley locations.</p>
    <p class="script front-signature">Dr. Rennick, Mila and Odete</p>

    <div class="brand front-brand"><span class="brand__dot"></span>BRIGHTLENS CARE</div>

    <div class="contact contact--phone">
      <svg width="26" height="26" viewBox="0 0 26 26"><circle cx="13" cy="13" r="11" fill="none" stroke="#e0212a" stroke-width="2"/><path d="M9 7 l3 3 -1.5 2 q1 2.5 3.5 3.5 l2-1.5 3 3 -2 2 q-6 0 -10-6 q-1-3 2-6z" fill="#e0212a"/></svg>
      509-418-2639
    </div>
    <div class="contact contact--email">
      <svg width="26" height="18" viewBox="0 0 26 18"><rect x="1" y="1" width="24" height="16" fill="#e0212a"/><path d="M1 1 L13 10 L25 1" fill="none" stroke="#fff" stroke-width="2"/></svg>
      hello@brightlenscare.com
    </div>
    <div class="contact contact--web">
      <svg width="22" height="22" viewBox="0 0 22 22" fill="none" stroke="#e0212a" stroke-width="1.6"><circle cx="11" cy="11" r="9.5"/><ellipse cx="11" cy="11" rx="4" ry="9.5"/><path d="M1.5 11 H20.5 M3 6 H19 M3 16 H19"/></svg>
      www.brightlenscare.com
    </div>
  </section>

  <section class="card card--back" aria-label="Postcard back">
    <svg class="card-art" width="790" height="558" viewBox="0 0 790 558" aria-hidden="true">
      <defs>
        <linearGradient id="backPanel" x1="0" y1="0" x2="0" y2="1">
          <stop offset="0" stop-color="#ffffff"/>
          <stop offset="0.42" stop-color="#ffffff"/>
          <stop offset="0.7" stop-color="#3d9cdb"/>
          <stop offset="1" stop-color="#0a7fc9"/>
        </linearGradient>
      </defs>
      <path d="M0 0 H300 Q384 60 384 170 V558 H0 Z" fill="url(#backPanel)"/>
      <path d="M0 0 H296 Q340 30 365 78 Q250 14 0 50 Z" fill="#0a7fc9"/>
      <path d="M0 50 Q250 14 365 78" fill="none" stroke="#1d3f8a" stroke-width="2"/>
      <path d="M300 0 Q384 60 384 170 V558" fill="none" stroke="#0a7fc9" stroke-width="2"/>
    </svg>

    <div class="brand back-brand"><span class="brand__dot"></span>BRIGHTLENS CARE</div>
    <p class="script back-find">Find us Here</p>

    <div class="clinic-photo clinic-photo--airway" role="img" aria-label="Airway Heights clinic interior with eye chart mural"></div>
    <div class="address-strip">
      <div class="address">
        <p class="address__name">Airway Heights Clinic</p>
        <p class="address__street">3094 S Pimbury Rd.</p>
      </div>
      <div class="address">
        <p class="address__name">Spokane Valley Clinic</p>
        <p class="address__street">48316 E Carrow Ln.</p>
      </div>
    </div>
    <div class="clinic-photo clinic-photo--valley" role="img" aria-label="Spokane Valley clinic front desk with eye chart mural"></div>

    <div class="stamp-box" aria-label="Stamp area"></div>
    <div class="mail-line" style="top:314px"></div>
    <div class="mail-line" style="top:368px"></div>
    <div class="mail-line" style="top:422px"></div>
    <div class="mail-line" style="top:475px"></div>
  </section>

</div>
</body>
</html>
```